Design mobile friendly review and ranking site

We're working on a corporate website for reviewing and ranking fellow employees. We need the website to look both fun and professional and it needs to be responsive - to it works on mobile and desktop.

Looking for css and HTML for 3 key pages as well as a header and footer for the site. Also would need any supporting graphics as part of the design.

Target Market(s)

Professionals in their 20s, 30s, and 40s.

Industry/Entity Type

Internet

Coding

Coded - Design and coding required

Number of Pages Required

3 page

Font styles to use
Sans Serif

Requirements
Must have
• 3 key pages we need (note included screenshots for each - these are just super rough cuts so you see examples of the content.)
• a) main-intro: A compelling into page with a login/registration form. Should be sleek/modern/enticing. Also we would show the ranking for the top 3 people to tease people re: content.
• b) main-page: Has two sections: One at the top where you would rate someone and one at the bottom where it shows a ranking of people.
• c) profile page: This is where you view a specific person. You see the person's picture, some info about the person, you see their overall rating, you can rate them, and you also see their historical ratings.
Nice to have
• Note we need css and HTML for this. It should feel as sleek and modern. Note also must be responsive design so it works well in mobile and desktop.

```html
<!DOCTYPE html>
<html lang="en">
<head>
<meta charset="utf-8">
<title>Peerly – Rate and Rank</title>
<link rel="stylesheet" href="https://fonts.googleapis.com/css2?family=Open+Sans:wght@400;600;700&display=swap">
<style>
  :root {
    --ink: #2b3640;
    --ink-soft: #4f5a63;
    --ink-muted: #7d848a;
    --brand-dark: #1c3a4f;
    --accent: #f57c00;
    --accent-blue: #2aa3d8;
    --link: #2aa3d8;
    --star-off: #858585;
    --btn-grey: #808080;
    --panel: #eceff2;
    --sidebar: #ffffff;
    --rule: #cfd4d8;
    --avatar-bg: #d6d6d6;
    --avatar-fg: #5f5f5f;
    --white: #ffffff;
  }
  * { box-sizing: border-box; margin: 0; padding: 0; }
  html, body { width: 1114px; height: 1200px; overflow: hidden; }
  body {
    font-family: "Open Sans", "Segoe UI", sans-serif;
    color: var(--ink);
    background: var(--panel);
    position: relative;
  }

  /* Sidebar */
  .sidebar {
    position: absolute; left: 0; top: 0;
    width: 231px; height: 1200px;
    background: var(--sidebar);
  }
  .brand {
    position: absolute; left: 22px; top: 20px;
    font-size: 42px; font-weight: 700; letter-spacing: 1px;
    color: var(--brand-dark); line-height: 1;
  }
  .user-avatar {
    position: absolute; left: 42px; top: 120px;
    width: 140px; height: 140px; border-radius: 50%;
    background: radial-gradient(circle at 50% 45%, var(--avatar-fg) 0 32%, var(--avatar-bg) 33%);
  }
  .user-name, .user-review {
    position: absolute; left: 0; width: 222px; text-align: center;
    font-size: 16px; color: var(--ink);
  }
  .user-name { top: 270px; }
  .user-review { top: 299px; }
  .account-links {
    position: absolute; left: 24px; top: 362px;
    font-size: 16px; color: var(--ink);
    display: flex; gap: 14px;
  }

  /* Rating panel */
  .rate-panel { position: absolute; left: 264px; top: 0; width: 807px; }
  .rate-title { position: absolute; top: 23px; left: 0; font-size: 18px; font-weight: 400; color: var(--ink); }
  .rule { position: absolute; left: 0; width: 807px; height: 1px; background: var(--rule); }
  .criterion {
    position: absolute; left: 1px; width: 700px; height: 34px;
    display: flex; align-items: center;
  }
  .criterion-label { width: 229px; font-size: 15.5px; color: var(--ink-soft); }
  .stars { display: flex; }
  .stars svg { display: block; }
  .stars--large svg { width: 31px; height: 31px; margin-right: 7px; }
  .stars--small svg { width: 21px; height: 21px; margin-right: 3.5px; }
  .star-on { fill: var(--accent); }
  .star-off { fill: var(--star-off); }
  .comment-label { position: absolute; top: 276px; left: 3px; font-size: 15.5px; color: var(--ink-soft); }
  .comment-box {
    position: absolute; top: 311px; left: 0;
    width: 532px; height: 139px;
    background: var(--white); border: 1px solid var(--rule); border-radius: 9px;
  }
  .btn {
    position: absolute; top: 483px; width: 109px; height: 45px;
    border: 0; border-radius: 3px; color: var(--white);
    font-family: inherit; font-size: 20px; letter-spacing: .5px;
  }
  .btn--skip { left: 2px; background: var(--accent); }
  .btn--save { left: 126px; background: var(--btn-grey); }

  /* Filter bar */
  .filter-bar {
    position: absolute; left: 231px; top: 562px;
    width: 883px; height: 67px; background: var(--accent-blue);
  }
  .select {
    position: absolute; top: 16px; height: 33px;
    background: var(--white); border-radius: 2px;
    font-size: 16px; color: var(--link);
    padding-left: 11px; line-height: 33px;
  }
  .select svg { position: absolute; right: 11px; top: 11px; width: 18px; height: 12px; fill: var(--link); }
  .filter-word { position: absolute; top: 20px; font-size: 16px; color: var(--white); }

  /* Ranking list */
  .rank-item { position: absolute; left: 231px; width: 883px; height: 180px; }
  .rank-badge { position: absolute; left: 31px; top: 23px; font-size: 13.5px; color: var(--link); }
  .rank-name {
    position: absolute; left: 29px; top: 45px; max-width: 160px;
    font-size: 23.5px; color: var(--ink-muted); white-space: nowrap;
  }
  .rank-avatar {
    position: absolute; left: 194px; top: 6px;
    width: 94px; height: 94px; border-radius: 50%;
    background: radial-gradient(circle at 50% 45%, var(--avatar-fg) 0 32%, var(--avatar-bg) 33%);
  }
  .rank-item--second .rank-badge { top: 32px; }
  .rank-item--second .rank-name { top: 54px; }
  .rank-item--second .rank-avatar { top: 29px; }
  .rank-item--third .rank-badge { top: 43px; }
  .rank-item--third .rank-name { top: 65px; }
  .rank-item--third .rank-avatar { top: 25px; }
  .rank-points { position: absolute; left: 360px; top: 2px; font-size: 13.5px; color: var(--ink); }
  .rank-reviews { position: absolute; left: 360px; top: 35px; font-size: 13.5px; color: var(--ink); }
  .rank-reviews a { color: var(--link); text-decoration: none; margin-left: 4px; }
  .score-row { position: absolute; left: 360px; width: 400px; height: 22px; display: flex; align-items: center; }
  .score-label { width: 227px; text-align: right; padding-right: 21px; font-size: 13.5px; color: var(--ink); }
  .list-rule { position: absolute; left: 264px; width: 807px; height: 1px; background: var(--rule); }
</style>
</head>
<body>
<svg width="0" height="0" style="position:absolute">
  <symbol id="star" viewBox="0 0 24 24"><path d="M12 1.2l3.3 7.1 7.7.9-5.7 5.3 1.5 7.7L12 18.4l-6.8 3.8 1.5-7.7L1 9.2l7.7-.9z"/></symbol>
  <symbol id="caret" viewBox="0 0 18 12"><path d="M0 0h18L9 12z"/></symbol>
</svg>

<aside class="sidebar">
  <div class="brand">PEERLY</div>
  <div class="user-avatar" role="img" aria-label="Profile photo of the signed-in user"></div>
  <div class="user-name">Daniel</div>
  <div class="user-review">View Review</div>
  <nav class="account-links"><span>Your Profile</span><span>|</span><span>Logout</span></nav>
</aside>

<section class="rate-panel">
  <h1 class="rate-title">Anonmously rate person for a point</h1>
  <div class="rule" style="top:61px"></div>

  <div class="criterion" style="top:91px">
    <span class="criterion-label">Smart</span>
    <span class="stars stars--large">
      <svg class="star-on"><use href="#star"/></svg><svg class="star-on"><use href="#star"/></svg><svg class="star-on"><use href="#star"/></svg><svg class="star-on"><use href="#star"/></svg><svg class="star-off"><use href="#star"/></svg>
    </span>
  </div>
  <div class="criterion" style="top:138px">
    <span class="criterion-label">Averagege Personality</span>
    <span class="stars stars--large">
      <svg class="star-on"><use href="#star"/></svg><svg class="star-on"><use href="#star"/></svg><svg class="star-on"><use href="#star"/></svg><svg class="star-off"><use href="#star"/></svg><svg class="star-off"><use href="#star"/></svg>
    </span>
  </div>
  <div class="criterion" style="top:185px">
    <span class="criterion-label">Work Crazy Hard</span>
    <span class="stars stars--large">
      <svg class="star-on"><use href="#star"/></svg><svg class="star-on"><use href="#star"/></svg><svg class="star-on"><use href="#star"/></svg><svg class="star-on"><use href="#star"/></svg><svg class="star-off"><use href="#star"/></svg>
    </span>
  </div>

  <div class="rule" style="top:250px"></div>
  <label class="comment-label">Optional Write an anonymous comment about this person</label>
  <div class="comment-box"></div>
  <button class="btn btn--skip">SKIP</button>
  <button class="btn btn--save">SAVE</button>
</section>

<div class="filter-bar">
  <div class="select" style="left:15px;width:124px">Best<svg><use href="#caret"/></svg></div>
  <span class="filter-word" style="left:163px">in</span>
  <div class="select" style="left:199px;width:223px">All Functions<svg><use href="#caret"/></svg></div>
  <span class="filter-word" style="left:436px">and</span>
  <div class="select" style="left:482px;width:225px">All Levels<svg><use href="#caret"/></svg></div>
</div>

<article class="rank-item" style="top:668px">
  <div class="rank-badge">#1 Best</div>
  <div class="rank-name">Tom Harlow</div>
  <div class="rank-avatar" role="img" aria-label="Profile photo of Tom Harlow"></div>
  <div class="rank-points">Points: 41</div>
  <div class="rank-reviews">Number of reviews : <a>5</a><a>View details</a></div>
  <div class="score-row" style="top:59px"><span class="score-label">Smarts</span><span class="stars stars--small"><svg class="star-on"><use href="#star"/></svg><svg class="star-on"><use href="#star"/></svg><svg class="star-on"><use href="#star"/></svg><svg class="star-on"><use href="#star"/></svg><svg class="star-off"><use href="#star"/></svg></span></div>
  <div class="score-row" style="top:84px"><span class="score-label">Easy to work with</span><span class="stars stars--small"><svg class="star-on"><use href="#star"/></svg><svg class="star-on"><use href="#star"/></svg><svg class="star-on"><use href="#star"/></svg><svg class="star-on"><use href="#star"/></svg><svg class="star-off"><use href="#star"/></svg></span></div>
  <div class="score-row" style="top:108px"><span class="score-label">Hard wordker</span><span class="stars stars--small"><svg class="star-on"><use href="#star"/></svg><svg class="star-on"><use href="#star"/></svg><svg class="star-on"><use href="#star"/></svg><svg class="star-on"><use href="#star"/></svg><svg class="star-off"><use href="#star"/></svg></span></div>
</article>
<div class="list-rule" style="top:829px"></div>

<article class="rank-item rank-item--second" style="top:843px">
  <div class="rank-badge">#2 Best</div>
  <div class="rank-name">Tom Harlow</div>
  <div class="rank-avatar" role="img" aria-label="Profile photo of Tom Harlow"></div>
  <div class="rank-points">Points: 4</div>
  <div class="rank-reviews">Number of reviews : <a>5</a><a>View details</a></div>
  <div class="score-row" style="top:59px"><span class="score-label">Smarts</span><span class="stars stars--small"><svg class="star-on"><use href="#star"/></svg><svg class="star-on"><use href="#star"/></svg><svg class="star-on"><use href="#star"/></svg><svg class="star-on"><use href="#star"/></svg><svg class="star-off"><use href="#star"/></svg></span></div>
  <div class="score-row" style="top:84px"><span class="score-label">Easy to work with</span><span class="stars stars--small"><svg class="star-on"><use href="#star"/></svg><svg class="star-on"><use href="#star"/></svg><svg class="star-on"><use href="#star"/></svg><svg class="star-on"><use href="#star"/></svg><svg class="star-off"><use href="#star"/></svg></span></div>
  <div class="score-row" style="top:108px"><span class="score-label">Hard wordker</span><span class="stars stars--small"><svg class="star-on"><use href="#star"/></svg><svg class="star-on"><use href="#star"/></svg><svg class="star-on"><use href="#star"/></svg><svg class="star-on"><use href="#star"/></svg><svg class="star-off"><use href="#star"/></svg></span></div>
</article>
<div class="list-rule" style="top:1014px"></div>

<article class="rank-item rank-item--third" style="top:1029px">
  <div class="rank-badge">#2 Best</div>
  <div class="rank-name">Ray Dunn III</div>
  <div class="rank-avatar" role="img" aria-label="Profile photo of Ray Dunn III"></div>
  <div class="rank-points">Points: 36</div>
  <div class="rank-reviews">Number of reviews : <a>5</a><a>View details</a></div>
  <div class="score-row" style="top:59px"><span class="score-label">Smarts</span><span class="stars stars--small"><svg class="star-on"><use href="#star"/></svg><svg class="star-on"><use href="#star"/></svg><svg class="star-on"><use href="#star"/></svg><svg class="star-on"><use href="#star"/></svg><svg class="star-off"><use href="#star"/></svg></span></div>
  <div class="score-row" style="top:84px"><span class="score-label">Easy to work with</span><span class="stars stars--small"><svg class="star-on"><use href="#star"/></svg><svg class="star-on"><use href="#star"/></svg><svg class="star-on"><use href="#star"/></svg><svg class="star-on"><use href="#star"/></svg><svg class="star-off"><use href="#star"/></svg></span></div>
  <div class="score-row" style="top:108px"><span class="score-label">Hard wordker</span><span class="stars stars--small"><svg class="star-on"><use href="#star"/></svg><svg class="star-on"><use href="#star"/></svg><svg class="star-on"><use href="#star"/></svg><svg class="star-on"><use href="#star"/></svg><svg class="star-off"><use href="#star"/></svg></span></div>
</article>
</body>
</html>
```